Brightpath Home & Upkeep Services, are a company that offers a 'one stop shop' pre-move clean up a

I have already selected a logo which I would like on the front of the business cards along with phone numbers, web address and email which are:
0419586402
www.brightpathhome.com.au
brightpathandupkeep@mailnest.com

On the back of the card I would like to list some of the types of service we offer (clean - move - repairs/maintenance) which are:
CLEAN - windows, gutters, solar panels, driveways/paths, carpets.
MOVE - Small/medium size house/office moves, large item pick-up & delivery, yard clean-up and removal.
General maintenance and repairs.

I would like the blue logo on a gray background.

Thanks

```html
<!DOCTYPE html>
<html lang="en">
<head>
<meta charset="utf-8">
<title>Brightpath Home &amp; Upkeep Services – Business Card</title>
<link rel="stylesheet" href="https://fonts.googleapis.com/css2?family=Josefin+Sans:wght@300;400;600;700&display=swap">
<style>
  :root {
    --stage: #3a3a3a;
    --card-white: #ffffff;
    --back-light: #f2f2f2;
    --back-shade: #c9c9c9;
    --brand-blue: #2f7fd0;
    --ink-dark: #2c2c2c;
    --ink-grey: #6b6b6b;
    --faint-box: #efefef;
  }
  * { box-sizing: border-box; margin: 0; padding: 0; }
  html, body {
    width: 1200px; height: 900px; overflow: hidden;
    background: var(--stage);
    font-family: "Josefin Sans", sans-serif;
  }
  .stage {
    width: 1200px; height: 900px;
    display: flex; flex-direction: column;
    align-items: center; justify-content: center; gap: 30px;
  }
  .card {
    width: 700px; height: 400px; position: relative;
    box-shadow: 0 10px 30px rgba(0,0,0,.45);
  }

  /* Back side */
  .card--back {
    background: linear-gradient(160deg, var(--back-light) 0%, #e4e4e4 55%, var(--back-shade) 100%);
    text-align: center; color: var(--ink-dark);
    padding-top: 70px;
  }
  .brand {
    display: inline-flex; align-items: center; gap: 10px;
    color: var(--brand-blue); font-weight: 700; font-size: 26px;
  }
  .brand__square { width: 18px; height: 18px; background: var(--brand-blue); }
  .services { margin-top: 50px; font-size: 15px; line-height: 1.5; font-weight: 400; }
  .services__heading { font-weight: 700; font-size: 16px; }
  .services__group + .services__group { margin-top: 14px; }

  /* Front side */
  .card--front { background: var(--card-white); }
  .card--front .brand { position: absolute; left: 45px; top: 100px; font-size: 22px; }
  .placeholder-box {
    position: absolute; left: 90px; top: 170px;
    width: 170px; height: 110px; background: var(--faint-box);
  }
  .website {
    position: absolute; left: 45px; bottom: 45px;
    font-size: 19px; color: var(--ink-grey); letter-spacing: .5px;
  }
  .contact { position: absolute; left: 410px; top: 135px; color: var(--ink-grey); }
  .contact__name { color: var(--brand-blue); font-size: 21px; font-weight: 600; margin-bottom: 14px; }
  .contact__name .role { font-weight: 400; }
  .contact__row {
    display: flex; align-items: flex-start; gap: 10px;
    font-size: 13.5px; font-weight: 300; line-height: 1.45; margin-bottom: 4px;
  }
  .contact__row svg { flex: none; margin-top: 2px; fill: var(--brand-blue); }
</style>
</head>
<body>
<main class="stage">
  <section class="card card--back">
    <div class="brand"><span class="brand__square"></span>Brightpath Home &amp; Upkeep Services</div>
    <div class="services">
      <div class="services__group">
        <div class="services__heading">CLEAN</div>
        <div>windows, gutters, solar panels, driveways/paths, carpets.</div>
      </div>
      <div class="services__group">
        <div class="services__heading">MOVE</div>
        <div>Small/medium size house/office moves, large item pick-up &amp; delivery,</div>
        <div>yard clean-up and removal. General maintenance and repairs.</div>
      </div>
    </div>
  </section>

  <section class="card card--front">
    <div class="brand"><span class="brand__square"></span>Brightpath Home &amp; Upkeep Services</div>
    <div class="placeholder-box"></div>
    <div class="website">www.brightpathhome.com.au</div>
    <div class="contact">
      <div class="contact__name">Sam Carter <span class="role">| President</span></div>
      <div class="contact__row">
        <svg width="12" height="16" viewBox="0 0 12 16"><path d="M6 0a6 6 0 0 0-6 6c0 4.5 6 10 6 10s6-5.5 6-10a6 6 0 0 0-6-6zm0 8.5A2.5 2.5 0 1 1 6 3.5a2.5 2.5 0 0 1 0 5z"/></svg>
        <div>Suit 12 Your Street 34 Your City<br>56 Country 78901</div>
      </div>
      <div class="contact__row">
        <svg width="14" height="12" viewBox="0 0 14 12"><path d="M1 3c0-2 12-2 12 0v1.5h-3V3H4v1.5H1zM2.5 5h9l1.5 7H1z"/></svg>
        <div>041 958 6402</div>
      </div>
      <div class="contact__row">
        <svg width="14" height="11" viewBox="0 0 14 11"><path d="M0 0h14v11H0zm1.5 1.5v.3L7 6l5.5-4.2v-.3zm0 2V9.5h11v-6L7 7.7z"/></svg>
        <div>brightpathandupkeep@mailnest.com</div>
      </div>
    </div>
  </section>
</main>
</body>
</html>
```